Help Give House Painter “Fresh” Website Makeover!

A residential and commercial painting company based in Albuquerque, NM, USA needs a fresh, new, fun, and playful--yet, simple, elegant and professional--website made.

Here is a link to their existing site:

http://corvelhomecoat.com/

We want to keep a similar site structure., So the navigation layout will stay the same. However, the video is too small, is too far over in the sidebar, and the overall design is amateur at best. We want something bright, colorful and bold!

We will need a space for the Video above the fold, and there needs to be space in the design for Testimonials, Specials and Images. It’s also very important to have the Angie’s List awards that you see on his current website.

Please also include somewhere in the Design icons for Reelio, Kinfeed, Orbitly and Proline.

Here are some examples to look at to get your creative juices flowing!

http://quillbrushworks.com/

http://www.tmvr.org/

http://www.marlowe-tasker.com/

http://www.plumtreepages.com/painting-company-plumtree-page/

http://www.quarrylanedesk.com/website-templates/painting-company-website-template-81735.html

We have accounts at both gleamvault.com and pixorra.com. If you use placeholder images from there, that's fine. We can buy the images when and if your design is selected.

Target Market(s)

The audience is the average middle class homeowner to higher upper class. This should appeal to families, couples, and singles who own a home.

Industry/Entity Type

Residential

Font styles to use
Sans Serif

Requirements
Must have
• - - Lots of color! It's a site about painting homes. People like a variety of colors. Bring out your inner artist, and get bold with your colors!

- - A video place holder. As you can see, there is a video on the existing site, but it's small and hidden. Make it big and put it top left, or in the center.

- -Detailed and organized PSD structure. We're going to turn your design into a website, and to make that work soothly, we ask that you organize you PSD well: name your layers, keep things separated, group and ungroup as necessary, etc.

- A sidebar that goes down the right side of an interior page. We need a homepage, and also one [1] interior page template. We don't need you to make a design for each page. Just the homepage, followed by a simple interior page design that requires only the header/navigation, and a sidebar down the right side.
Should not have
• - Coding. This is a design project only.

```html
<!DOCTYPE html>
<html lang="en">
<head>
<meta charset="utf-8">
<title>Wade's Painting – Albuquerque House Painters</title>
<link href="https://fonts.googleapis.com/css2?family=Varela+Round&family=Quicksand:wght@400;500;600&display=swap" rel="stylesheet">
<style>
:root{
  --blue:#1a3f9e;
  --blue-dark:#143283;
  --nav:#1c4fb0;
  --red:#e3101f;
  --orange:#e8870d;
  --orange-btn:#f39413;
  --panel:#d3e1ee;
  --ink:#333;
  --muted:#555;
  --white:#fff;
}
*{box-sizing:border-box;margin:0;padding:0}
html,body{width:742px;height:1200px;overflow:hidden;background:#fff}
body{position:relative;font-family:"Quicksand",sans-serif;color:var(--ink)}
h1,h2,h3{font-family:"Varela Round",sans-serif;font-weight:400}
.abs{position:absolute}

/* header */
.top{left:0;top:0;width:742px;height:61px;background:linear-gradient(#fff,#dfeaf5)}
.brand{left:50px;top:13px;display:flex;gap:9px;align-items:center}
.brand-dot{width:34px;height:34px;border-radius:50%;background:var(--blue)}
.brand-name{font-family:"Varela Round",sans-serif;font-size:16px;color:var(--blue);line-height:1.2}
.phone-top{left:93px;top:35px;font-family:"Quicksand",sans-serif;font-weight:600;font-size:11px;color:var(--red)}
.cta-top{right:57px;top:20px;background:#1b1b1b;color:#fff;font-size:9.5px;padding:8px 11px;letter-spacing:.3px}
nav{left:0;top:61px;width:742px;height:29px;background:linear-gradient(var(--nav),var(--blue-dark));display:flex;align-items:center;padding-left:53px;gap:25px}
nav a{color:#fff;font-size:8.2px;text-decoration:none;letter-spacing:.3px}

/* hero */
.hero-photo{left:0;top:90px;width:742px;height:256px;background:linear-gradient(100deg,#c9d2df 0%,#9aa9c9 25%,#4f79d4 45%,#e7e8ee 78%,#f5f4f0 100%)}
.estimate{left:241px;top:154px;width:261px;height:145px;background:rgba(214,230,246,.82);text-align:center;padding-top:12px}
.estimate h1{font-size:21px;color:var(--blue);font-weight:700}
.estimate p{font-family:"Varela Round",sans-serif;font-size:12.5px;color:#222;line-height:1.35;margin-top:2px}
.estimate .call{display:inline-flex;align-items:center;gap:6px;margin-top:9px;background:var(--orange-btn);color:#fff;font-size:17px;padding:5px 13px;font-family:"Varela Round",sans-serif}
.award{left:530px;width:167px;height:75px;background:var(--red);display:flex;align-items:center;gap:8px;padding-left:12px;color:#fff;font-family:"Varela Round",sans-serif;font-size:11.5px;text-align:center;line-height:1.4}
.award .seal{width:44px;height:54px;border-radius:4px;background:#c9a43a;flex:none}
.award span{flex:1}
.dots{left:350px;top:326px;display:flex;gap:4px}
.dots i{width:9px;height:9px;border-radius:50%;background:#333}
.dots i:first-child{background:var(--red)}

/* intro */
.intro{left:46px;top:368px;width:430px}
.intro h2{font-size:17px;color:var(--blue);margin-bottom:9px}
.intro p{font-size:7.3px;line-height:1.78;color:var(--muted);margin-bottom:6px}
.intro .hot{color:var(--red);font-size:8px}
.video{left:491px;top:368px;width:206px}
.video h2{font-size:17px;color:var(--blue);margin-bottom:12px}
.video-frame{width:206px;height:133px;border:1px solid #aaa;background:linear-gradient(#dfe3e8,#bcc4cd);position:relative}
.video-band{position:absolute;left:0;bottom:18px;width:100%;height:20px;background:#3a3126;color:#d9c9a8;font-size:9px;letter-spacing:1.5px;text-align:center;line-height:20px}
.play{position:absolute;left:87px;top:47px;width:32px;height:32px;border-radius:6px;background:rgba(0,0,0,.55)}

/* features */
.features{left:0;top:555px;width:742px;height:257px;background:var(--orange)}
.card{top:581px;width:204px;color:#fff}
.card .pic{width:204px;height:100px}
.card h3{font-size:10.5px;margin-top:12px;line-height:1.5;letter-spacing:.2px}
.card p{font-size:7.3px;line-height:1.75;margin-top:5px;color:#fde6c6}
.btn-blue{display:inline-block;background:var(--blue);color:#fff;font-size:8px;padding:7px 11px;margin-top:10px;letter-spacing:.3px}

/* lower */
.specials{left:46px;top:834px;width:204px;height:256px;background:var(--panel);padding:13px 17px}
.specials h2{font-size:17px;color:var(--blue);margin-bottom:9px}
.specials .pic{width:176px;height:80px}
.specials p{font-size:8.8px;line-height:1.55;color:#333;margin-top:13px}
.btn-red{display:inline-block;background:var(--red);color:#fff;font-size:9px;padding:7px 10px;margin-top:10px}
.gallery{left:268px;top:830px;width:429px}
.gallery h2{font-size:16.5px;color:var(--blue)}
.arrows{position:absolute;right:0;top:4px}
.thumbs{display:flex;gap:10px;margin-top:11px}
.thumbs div{width:136px;height:77px;border:1px solid #bbb}
.rule{left:268px;top:957px;width:429px;height:1px;background:#ccc}
.testis{left:268px;top:968px;width:429px}
.testis h2{font-size:17px;color:var(--blue);margin-bottom:12px}
.trow{display:flex;gap:17px}
.testi{width:132px}
.testi h4{font-weight:500;font-size:9.3px;color:var(--red);line-height:1.45}
.testi p{font-size:7.2px;line-height:1.6;margin-top:6px;color:#444}
.testi .by{display:flex;align-items:center;gap:7px;margin-top:5px;font-size:7.3px;color:var(--blue)}

/* footer */
footer{left:0;top:1111px;width:742px;height:89px;background:var(--blue-dark)}
.flinks{left:46px;top:1132px;color:#fff;font-size:8px;word-spacing:2px}
.copy{left:46px;top:1157px;color:#dce4f5;font-size:7.3px;line-height:1.8}
.connect{left:605px;top:1127px;color:#fff;font-size:7px}
.socials{left:605px;top:1145px;display:flex;gap:5px}
.socials span{background:#fff;color:var(--blue-dark);font-size:5.6px;padding:4px 2px;width:24px;text-align:center}
</style>
</head>
<body>

<header class="abs top"></header>
<div class="abs brand">
  <div class="brand-dot"></div>
  <div class="brand-name">Wade's Painting</div>
</div>
<div class="abs phone-top">505-555-0142</div>
<div class="abs cta-top">GET FREE ESTIMATE</div>

<nav class="abs">
  <a>HOME</a><a>ABOUT US</a><a>RESIDENTIAL PAINTING</a><a>COMMERCIAL PAINTING</a><a>FAQ</a><a>SPECIAL</a><a>BLOG</a><a>TESTIMONIALS</a><a>CONTACT US</a>
</nav>

<div class="abs hero-photo" role="img" aria-label="Blue paint roller rolling paint across a wall above white trim"></div>
<div class="abs estimate">
  <h1>Get A Free Estimate</h1>
  <p>Need Painting in the Albuquerque<br>Area? Call Wade today for your FREE<br>painting estimate!</p>
  <div class="call">
    <svg width="14" height="12" viewBox="0 0 14 12"><path d="M1 4c0-2 2-3 6-3s6 1 6 3l-3 1-1-2H5L4 5zM3 6h8l1 5H2z" fill="#fff"/></svg>555-0142
  </div>
</div>
<div class="abs award" style="top:138px"><div class="seal" role="img" aria-label="Brindle Ledger service award badge"></div><span>Best<br>Exterior Painting<br>Awards</span></div>
<div class="abs award" style="top:219px"><div class="seal" role="img" aria-label="Brindle Ledger service award badge"></div><span>Best<br>Interior Painting<br>Awards</span></div>
<div class="abs dots"><i></i><i></i><i></i><i></i></div>

<section class="abs intro">
  <h2>Wade's Painting in Albuquerque, New Mexico</h2>
  <p>Wade's Painting does jobs as small as a bathroom up to large commercial projects right here in Albuquerque and Rio Rancho. Extensive as an entire apartment exterior, to a kitchen and all home interior, no job is too big or too small for Wade's Painting of Albuquerque. Wade's Painting is staffed with the best painters for the highest quality paint jobs. Wade's Painting is not a community's average house painter staffing company, but this painting company is staffed with professional painters that pride themselves on successfully completing every job.</p>
  <p>We have also had the honor of receiving the Brindle Ledger Super Service Award for both Exterior and Interior painting in and around the Albuquerque, New Mexico area for the past 3 years. Wade's Painting is a Civic Trade Registry (CTR) accredited commercial painting company as well, and is listed in the Rio Grande Trade Circle. Clients can receive a free estimate if you need a paint job in the Albuquerque or Rio Rancho Area.</p>
  <p class="hot">Call Wade today at 555-0142 for your FREE painting estimate!</p>
</section>

<section class="abs video">
  <h2>Watch a Video</h2>
  <div class="video-frame" role="img" aria-label="Video still of the company owner speaking to camera">
    <div class="play"><svg width="32" height="32" viewBox="0 0 32 32"><path d="M12 9l11 7-11 7z" fill="#fff"/></svg></div>
    <div class="video-band">Wade - Wade's Painting</div>
  </div>
</section>

<div class="abs features"></div>
<article class="abs card" style="left:46px">
  <div class="pic" role="img" aria-label="Green paint roller on a freshly painted wall" style="background:linear-gradient(120deg,#b9e27a,#7cc43a)"></div>
  <h3>OUR PAINTING IN ALBUQUERQUE</h3>
  <p>Wade's Painting does jobs as small as a bathroom up to large commercial projects right here in Albuquerque...</p>
  <span class="btn-blue">READ MORE</span>
</article>
<article class="abs card" style="left:268px">
  <div class="pic" role="img" aria-label="Painter rolling white paint onto a ceiling" style="background:linear-gradient(120deg,#d9cbb8,#efece6)"></div>
  <h3>ALBUQUERQUE PAINTER VIDEOS</h3>
  <p>TWe have shot a ton of videos with Wade answering all of our most frequently asked questions.<br>We want to give them to you for FREE. All you have to do is..</p>
  <span class="btn-blue">READ MORE</span>
</article>
<article class="abs card" style="left:493px">
  <div class="pic" role="img" aria-label="Happy couple holding green paint rollers" style="background:linear-gradient(120deg,#9ed05a,#e8d8c8 60%,#8fc64a)"></div>
  <h3>HAPPY ALBUQUERQUE PAINTING CUSTOMERS</h3>
  <p>100% Customer Satisfaction is our Ultimate Goal. We are proud to have served so many clients in an around the Albuquerque..</p>
  <span class="btn-blue">READ MORE</span>
</article>

<aside class="abs specials">
  <h2>Wade's Painting</h2>
  <div class="pic" role="img" aria-label="Open paint cans in orange, blue and lilac with a brush" style="background:linear-gradient(100deg,#d46a2a,#9bb0c9 45%,#b9a9d9)"></div>
  <p>Free massage with any interior painting project over $1000.<br>The holidays are over. The guests are gone. It is time to pack up the decorations. And you notice the walls need a new coat of paint.</p>
  <span class="btn-red">CHECK OUT OUR SPECIALS</span>
</aside>

<section class="abs gallery">
  <h2>Image Gallery</h2>
  <svg class="arrows" width="30" height="12" viewBox="0 0 30 12"><path d="M7 1 2 6l5 5M23 1l5 5-5 5" fill="none" stroke="#666" stroke-width="1.2"/></svg>
  <div class="thumbs">
    <div role="img" aria-label="Painted castle-style building exterior" style="background:linear-gradient(#9fb8d6,#8a8c8f)"></div>
    <div role="img" aria-label="Stucco apartment building sign" style="background:linear-gradient(90deg,#777,#b9a79a)"></div>
    <div role="img" aria-label="Freshly painted kitchen interior" style="background:linear-gradient(#c9b58c,#6b5638)"></div>
  </div>
</section>
<div class="abs rule"></div>

<section class="abs testis">
  <h2>Testimonials</h2>
  <div class="trow">
    <div class="testi"><h4>Excellent work and an excellent price.</h4><p>Excellent work and an excellent price. We had a small area of stucco that fell off about a year after being painted...</p><div class="by">- Nora Pell <svg width="56" height="9" viewBox="0 0 56 9"><g fill="#f2c200"><path id="s" d="M4.5 0l1.3 3h3.2L6.4 5l1 3.6-2.9-2-2.9 2 1-3.6L0 3h3.2z"/><use href="#s" x="11.5"/><use href="#s" x="23"/><use href="#s" x="34.5"/><use href="#s" x="46"/></g></svg></div></div>
    <div class="testi"><h4>Excellent work and an excellent price.</h4><p>Excellent work and an excellent price. We had a small area of stucco that fell off about a year after being painted...</p><div class="by">- Nora Pell <svg width="56" height="9" viewBox="0 0 56 9"><g fill="#f2c200"><use href="#s"/><use href="#s" x="11.5"/><use href="#s" x="23"/><use href="#s" x="34.5"/><use href="#s" x="46"/></g></svg></div></div>
    <div class="testi"><h4>Excellent work and an excellent price.</h4><p>Excellent work and an excellent price. We had a small area of stucco that fell off about a year after being painted...</p><div class="by">- Nora Pell <svg width="56" height="9" viewBox="0 0 56 9"><g fill="#f2c200"><use href="#s"/><use href="#s" x="11.5"/><use href="#s" x="23"/><use href="#s" x="34.5"/><use href="#s" x="46"/></g></svg></div></div>
  </div>
</section>

<footer class="abs"></footer>
<div class="abs flinks">Home &nbsp;/ &nbsp;About Us &nbsp;/ &nbsp;FAQ &nbsp;/ &nbsp;Discounts &nbsp;/ &nbsp;Blog &nbsp;/ &nbsp;Testimonials &nbsp;/ &nbsp;Contact</div>
<div class="abs copy">Copyright © 2015.Company Name. All Right Reserved<br>Term of Services</div>
<div class="abs connect">CONNECT US</div>
<div class="abs socials"><span>Kinfeed</span><span>Proline</span><span>Orbitly</span><span>Reelio</span></div>

</body>
</html>
```